Home Remodeler Needs a Website!

Single page (plus contact form) website for small home remodeling company. He's got a few pictures he'd like on the site and needs some basic text. He likes clean, simple designs and is "more traditional" in his stylistic preferences. Most of his business comes from word-of-mouth advertising and so the site is just something he needs for people to feel more comfortable with his business.

Target Market(s)

People who want to remodel their homes

Coding

Coded - Design and coding required

Number of Pages Required

2 page

Requirements
Must have
• Main page to include some or all of the attached images, contact page. Neutral colors. Old domain: brindlecoveabodes.com New domain: qm-holdings.com You can pull text from the old site or update it.
Should not have
• No loud colors/loud visual elements

```html
<!DOCTYPE html>
<html lang="en">
<head>
<meta charset="utf-8">
<title>Brindle Cove Abodes</title>
<link href="https://fonts.googleapis.com/css2?family=Oswald:wght@300;400;500&family=Jost:wght@400;500&display=swap" rel="stylesheet">
<style>
:root{
  --blue:#1a6fba;
  --blue-dark:#0d4f8c;
  --ink:#222222;
  --text:#555555;
  --light:#f2f2f2;
  --white:#ffffff;
  --footer:#242424;
}
*{margin:0;padding:0;box-sizing:border-box}
html,body{width:1200px;height:4831px;overflow:hidden}
body{position:relative;background:var(--white);font-family:"Jost",sans-serif;color:var(--text)}
.abs{position:absolute}
.head{font-family:"Oswald",sans-serif;font-weight:400;color:var(--ink);text-transform:none}
.eyebrow{font-family:"Oswald",sans-serif;font-size:15px;color:var(--blue);letter-spacing:.5px}
.title{font-family:"Oswald",sans-serif;font-size:40px;font-weight:400;color:var(--ink);line-height:1}
.title .hl{color:var(--blue)}
.btn{display:inline-block;font-family:"Jost",sans-serif;font-size:16px;background:var(--blue);color:#fff;border-radius:5px;padding:0 14px;line-height:50px;text-transform:uppercase}
.btn-outline{font-family:"Oswald",sans-serif;font-size:15px;border:2px solid #555;color:#444;border-radius:6px;line-height:38px;padding:0 16px;display:inline-block;background:#fff}
p{font-size:12.5px;line-height:25px}

/* header */
.site-header{left:0;top:0;width:1200px;height:98px;background:#fff}
.brand{left:150px;top:32px;font-family:"Oswald",sans-serif;font-size:24px;color:var(--blue);display:flex;align-items:center;gap:10px}
.brand .mark{width:14px;height:14px;background:var(--blue)}
.nav{left:518px;top:0;display:flex;height:98px}
.nav a{font-family:"Oswald",sans-serif;font-size:14px;color:var(--ink);text-decoration:none;line-height:108px;padding:0 12px}
.nav a.active{background:var(--blue);color:#fff;padding:0 16px}

/* hero */
.hero{left:0;top:98px;width:1200px;height:562px;background:linear-gradient(180deg,#3c3630 0%,#4b4138 45%,#2d2824 100%)}
.hero-title{left:370px;top:268px;width:460px;height:90px;background:var(--blue);color:#fff;font-family:"Oswald",sans-serif;font-size:52px;text-align:center;line-height:90px}

/* about */
.about{left:172px;top:755px;width:400px}
.about .title{margin-top:8px;font-size:38px}
.about p{margin-top:14px}
.about .btn{margin-top:20px}
.booking{left:632px;top:720px;width:396px;height:460px;background:#fff;box-shadow:0 2px 12px rgba(0,0,0,.15);padding:20px 20px}
.booking h2{font-family:"Jost",sans-serif;font-weight:500;font-size:27px;color:var(--blue)}
.booking label{display:block;font-size:13px;color:#333;margin-top:24px}
.booking .field{margin-top:10px;height:42px;border:1.5px solid #888;border-radius:5px}
.booking .field.tall{height:88px}
.booking .submit{margin-top:20px;display:inline-block;background:var(--blue);color:#fff;font-size:14px;border-radius:4px;padding:0 18px;line-height:42px}

/* services */
.services{left:0;top:1262px;width:1200px;height:624px;background:var(--light)}
.center{width:1200px;text-align:center}
.svc-card{top:1464px;width:263px;height:316px;background:#fff;box-shadow:0 2px 8px rgba(0,0,0,.08);padding:32px 20px}
.svc-card h3{font-family:"Jost",sans-serif;font-weight:500;font-size:18px;color:var(--ink);margin-top:16px}
.svc-card p{font-size:12px;line-height:20px;margin-top:10px;text-align:justify}
.svc-card .btn-outline{margin-top:18px}
.svc-card.featured{background:linear-gradient(180deg,#1a72c0,#0d4f8c);color:#fff}
.svc-card.featured h3,.svc-card.featured p{color:#fff}
.svc-card.featured .btn-outline{border-color:#fff;color:#1a6fba}

/* commercial */
.frame-line{background:#333}
.photo{border:0}
.commercial{left:598px;top:1990px;width:430px}
.commercial .title{font-size:40px;margin-top:6px}
.commercial p{margin-top:14px}
.commercial .btn{margin-top:20px}

/* residential */
.res-band{left:0;top:2505px;width:1200px;height:439px;background:linear-gradient(90deg,#2a2622,#1d1b1a 50%,#2b2a2c)}
.res-card{top:2738px;width:263px;height:459px;background:#fff;box-shadow:0 2px 8px rgba(0,0,0,.12)}
.res-card .img{height:206px}
.res-card .body{padding:18px 14px}
.res-card h3{font-family:"Oswald",sans-serif;font-weight:400;font-size:18px;color:var(--ink)}
.res-card p{font-size:12px;line-height:20px;margin-top:10px;text-align:justify}
.res-card .btn-outline{margin-top:18px;font-size:15px}
.res-card .btn-outline.solid{background:var(--blue);border-color:var(--blue);color:#fff}

/* other services */
.step{width:240px;text-align:center}
.step .circle{width:94px;height:94px;border-radius:50%;margin:0 auto;display:flex;align-items:center;justify-content:center}
.step .circle.dark{background:#3a3a3a}
.step .circle.blue{background:var(--blue)}
.step h4{font-family:"Oswald",sans-serif;font-weight:400;font-size:21px;color:var(--ink);margin-top:16px}
.step h4.blue{color:var(--blue)}
.step p{font-size:12px;line-height:21px;margin-top:6px}

/* testimonials */
.testimonials{left:0;top:3840px;width:1200px;height:456px;background:linear-gradient(180deg,#294f7c,#1b4e86 50%,#1d5494)}
.tframe{background:#fff}
.arrow{width:40px;height:40px;background:#fff;transform:rotate(45deg)}
.quote-text{left:250px;top:4112px;width:700px;text-align:center;color:#fff;font-size:13.5px;line-height:25px}

/* footer */
.footer{left:0;top:4296px;width:1200px;height:535px;background:var(--footer)}
.foot-brand{left:172px;top:4450px;font-family:"Oswald",sans-serif;font-size:34px;color:#fff;display:flex;align-items:center;gap:12px}
.foot-brand .mark{width:16px;height:16px;background:#fff}
.foot-text{left:172px;top:4508px;width:430px;color:#fff;font-size:12px;line-height:28px}
.links h5{font-family:"Oswald",sans-serif;font-weight:400;font-size:22px;color:#fff}
.links ul{list-style:none;margin-top:22px}
.links li{font-family:"Oswald",sans-serif;font-size:13px;color:#fff;line-height:30px}
.copy{left:0;top:4778px;width:1200px;text-align:center;color:#fff;font-size:13px}
</style>
</head>
<body>

<header class="abs site-header">
  <div class="abs brand"><span class="mark"></span>Brindle Cove Abodes</div>
  <nav class="abs nav">
    <a class="active">HOME</a><a>ABOUT</a><a>SERVICES</a><a>GALLERY</a><a>TESTIMONIALS</a><a>AWARDS</a><a>CONTACT US</a>
  </nav>
</header>

<section class="abs hero" role="img" aria-label="Photo of a remodeled open-plan kitchen and living room with dark wood floors"></section>
<div class="abs hero-title">"ALL IN ONE PACKAGE"</div>
<svg class="abs" style="left:0;top:560px" width="1200" height="110" viewBox="0 0 1200 110">
  <path d="M0 100 Q600 30 1200 100 L1200 110 L0 110Z" fill="#fff"/>
  <path d="M0 100 Q600 20 1200 70 L1200 86 Q600 42 0 102Z" fill="#1a6fba"/>
</svg>

<section class="abs about">
  <div class="eyebrow">ABOUT</div>
  <div class="title"><span class="hl">BRINDLE</span> Cove Abodes</div>
  <p>With over 20 years experience in residential and commercial construction, you can trust your project to Brindle Cove Abodes. I have built my business with a partnership of clients, employees, subcontractors, suppliers and inspectors. Since each project is unique, this partnership brings creative ideas to your home.</p>
  <p style="margin-top:6px">I have deep "hands on" history in construction from foundations to final finishing touches. We cultivate suppliers who deliver quality materials on time and without damage. Our subcontractors are our friends and will become yours too.</p>
  <span class="btn">Read More</span>
</section>

<form class="abs booking">
  <h2>Book An Appointment</h2>
  <label>Your Name (required)</label><div class="field"></div>
  <label>Email Address (required)</label><div class="field"></div>
  <label>Your Message</label><div class="field tall"></div>
  <span class="submit">Submit</span>
</form>

<section class="abs services"></section>
<div class="abs center" style="left:0;top:1343px"><div class="eyebrow">ABOUT</div></div>
<div class="abs center title" style="left:0;top:1370px"><span class="hl">BRINDLE</span> Cove Services</div>

<div class="abs svc-card" style="left:172px">
  <svg width="50" height="50" viewBox="0 0 50 50" fill="none" stroke="#333" stroke-width="2.5"><circle cx="25" cy="25" r="22"/><path d="M13 26 L25 15 L37 26 M17 23 V35 H33 V23"/><rect x="22" y="27" width="6" height="8"/></svg>
  <h3>NEW CONSTRUCTION</h3>
  <p>Nemo enim ipsam voluptatem quia voluptas sit aspernatur aut odit aut fugit, sed quia consequuntur magni dolores eos qui voluptatem.</p>
  <span class="btn-outline">READ MORE</span>
</div>
<div class="abs svc-card featured" style="left:469px">
  <svg width="50" height="50" viewBox="0 0 50 50" fill="none" stroke="#fff" stroke-width="2.5"><path d="M14 18 Q25 4 36 18 Z"/><circle cx="25" cy="25" r="7"/><path d="M12 46 V38 Q25 28 38 38 V46"/></svg>
  <h3>KITCHENS AND BATHS</h3>
  <p>Nemo enim ipsam voluptatem quia voluptas sit aspernatur aut odit aut fugit, sed quia consequuntur magni dolores eos qui voluptatem.</p>
  <span class="btn-outline">READ MORE</span>
</div>
<div class="abs svc-card" style="left:763px">
  <svg width="50" height="50" viewBox="0 0 50 50" fill="none" stroke="#333" stroke-width="2.5"><circle cx="25" cy="26" r="9"/><circle cx="25" cy="26" r="16" stroke-dasharray="6 4"/><path d="M10 12 L18 6 L26 12"/></svg>
  <h3>RESIDENTIAL CONTRACTING</h3>
  <p>Nemo enim ipsam voluptatem quia voluptas sit aspernatur aut odit aut fugit, sed quia consequuntur magni dolores eos qui voluptatem.</p>
  <span class="btn-outline">READ MORE</span>
</div>

<div class="abs frame-line" style="left:172px;top:1984px;width:2px;height:431px"></div>
<div class="abs frame-line" style="left:172px;top:2413px;width:376px;height:2px"></div>
<div class="abs photo" style="left:190px;top:1969px;width:358px;height:427px;background:linear-gradient(160deg,#2c4f8a 0%,#6f7680 45%,#4a3428 100%)" role="img" aria-label="Photo of a kitchen with a stainless steel refrigerator and dark wood cabinets"></div>
<section class="abs commercial">
  <div class="eyebrow">OUR</div>
  <div class="title"><span class="hl">COMMERCIAL</span> Contracting</div>
  <p>Nemo enim ipsam voluptatem quia voluptas sit aspernatur aut odit aut fugit, sed quia consequuntur magni dolores eos qui ratione voluptatem sequi nesciunt. Neque porro quisquam est, qui dolorem ipsum quia dolor sit amet, consectetur, adipisci velit, sed quia non numquam eius modi tempora incidunt ut labore et dolore magnam aliquam quaerat voluptatem.</p>
  <p style="margin-top:6px">Neque porro quisquam est, qui dolorem ipsum quia dolor sit amet, consectetur, adipisci velit, sed quia non numquam eius modi tem pora incidunt ut labore.</p>
  <span class="btn">Read More</span>
</section>

<section class="abs res-band" role="img" aria-label="Dim photo of a stone-walled wine cellar"></section>
<div class="abs center" style="left:0;top:2583px;color:#fff;font-family:'Oswald',sans-serif;font-size:15px">OUR</div>
<div class="abs center title" style="left:0;top:2612px;color:#fff">RESIDENTIAL <span style="font-weight:300">Contracting</span></div>

<div class="abs res-card" style="left:172px">
  <div class="img" style="background:linear-gradient(180deg,#c9d2d6,#8f9ea4)" role="img" aria-label="Photo of a renovated bathroom with a soaking tub"></div>
  <div class="body"><h3>KITCHENS AND BATHS</h3><p>Sed ut perspiciatis unde omnis iste natus error sit voluptatem accusantium doloremque laudantium quae ab illo in ventore veritatis et quasi architecto beatae.</p><span class="btn-outline">Read More</span></div>
</div>
<div class="abs res-card" style="left:469px">
  <div class="img" style="background:linear-gradient(180deg,#7e9fc2,#35566b 60%,#4f5a4e)" role="img" aria-label="Photo of a two-storey house with a porch under renovation"></div>
  <div class="body"><h3>PORCHES AND DECKS</h3><p>Sed ut perspiciatis unde omnis iste natus error sit voluptatem accusantium doloremque laudantium quae ab illo in ventore veritatis et quasi architecto beatae.</p><span class="btn-outline solid">Read More</span></div>
</div>
<div class="abs res-card" style="left:763px">
  <div class="img" style="background:linear-gradient(180deg,#eae6e0,#b9b2a8 60%,#3d3934)" role="img" aria-label="Photo of a bright kitchen with an island and bar stools"></div>
  <div class="body"><h3>WINDOW REPLACEMENT</h3><p>Sed ut perspiciatis unde omnis iste natus error sit voluptatem accusantium doloremque laudantium quae ab illo in ventore veritatis et quasi architecto beatae.</p><span class="btn-outline">Read More</span></div>
</div>

<div class="abs center" style="left:0;top:3303px"><div class="eyebrow">OUR</div></div>
<div class="abs center title" style="left:0;top:3332px"><span class="hl">OTHER</span> Contracting Services</div>
<svg class="abs" style="left:0;top:3400px" width="1200" height="220" viewBox="0 0 1200 220" fill="none" stroke="#1a6fba" stroke-width="2.5">
  <path d="M310 80 Q360 150 420 160"/>
  <path d="M535 160 Q595 175 650 160"/>
  <path d="M760 160 Q840 150 880 80"/>
</svg>
<div class="abs step" style="left:148px;top:3399px">
  <div class="circle dark"><svg width="46" height="40" viewBox="0 0 46 40" fill="none" stroke="#fff" stroke-width="2.5"><path d="M3 20 L23 4 L43 20 M9 16 V36 H37 V16"/><rect x="18" y="22" width="10" height="14"/></svg></div>
  <h4>ROOFING</h4><p>With over 20 years experience in residential and commercial construction.</p>
</div>
<div class="abs step" style="left:360px;top:3519px">
  <div class="circle blue"><svg width="44" height="44" viewBox="0 0 44 44" fill="none" stroke="#fff" stroke-width="2.5"><path d="M8 6 V26 Q8 36 20 36 H38 M16 6 V24 Q16 28 20 28 H38"/></svg></div>
  <h4 class="blue">PLUMBING UPGRADES</h4><p>With over 20 years experience in residential and commercial construction.</p>
</div>
<div class="abs step" style="left:585px;top:3519px">
  <div class="circle dark"><svg width="44" height="44" viewBox="0 0 44 44" fill="none" stroke="#fff" stroke-width="2.5"><path d="M4 22 L22 6 L40 22 M10 18 V38 H34 V18"/><rect x="17" y="22" width="14" height="6"/><path d="M24 28 V36"/></svg></div>
  <h4>PAINTING</h4><p>With over 20 years experience in residential and commercial construction.</p>
</div>
<div class="abs step" style="left:810px;top:3399px">
  <div class="circle blue"><svg width="48" height="40" viewBox="0 0 48 40" fill="none" stroke="#fff" stroke-width="2.5"><rect x="4" y="6" width="40" height="16" rx="2"/><path d="M10 16 H38 M16 28 V34 M24 28 V36 M32 28 V34"/></svg></div>
  <h4 class="blue">AIR CONDITIONING</h4><p>With over 20 years experience in residential and commercial construction.</p>
</div>

<section class="abs testimonials" role="img" aria-label="Blue-tinted photo of a dining area and wine shelves"></section>
<div class="abs tframe" style="left:172px;top:3840px;width:2px;height:486px"></div>
<div class="abs tframe" style="left:1025px;top:3840px;width:2px;height:486px"></div>
<div class="abs tframe" style="left:172px;top:4324px;width:855px;height:2px"></div>
<div class="abs arrow" style="left:153px;top:4046px"></div>
<div class="abs arrow" style="left:1006px;top:4046px"></div>
<svg class="abs" style="left:161px;top:4054px" width="24" height="24" viewBox="0 0 24 24" fill="none" stroke="#333" stroke-width="2"><path d="M15 4 L7 12 L15 20"/></svg>
<svg class="abs" style="left:1015px;top:4054px" width="24" height="24" viewBox="0 0 24 24" fill="none" stroke="#333" stroke-width="2"><path d="M9 4 L17 12 L9 20"/></svg>
<div class="abs center" style="left:0;top:3933px;color:#fff;font-family:'Oswald',sans-serif;font-size:15px">OUR</div>
<div class="abs center title" style="left:0;top:3962px;color:#fff"><span style="font-weight:300">CLIENT</span> Testimonials</div>
<svg class="abs" style="left:570px;top:4040px" width="62" height="48" viewBox="0 0 62 48" fill="#fff"><path d="M2 48 V26 Q2 6 22 2 L24 8 Q12 12 12 22 H26 V48Z M36 48 V26 Q36 6 56 2 L58 8 Q46 12 46 22 H60 V48Z"/></svg>
<div class="abs quote-text">Nemo enim ipsam voluptatem quia voluptas sit aspernatur aut odit aut fugit, sed quia consequuntur magni dolores eos qui ratione voluptatem sequi nesciunt.<br><span style="display:block;margin-top:12px;font-size:16px">- MERCER</span></div>

<footer class="abs footer"></footer>
<div class="abs foot-brand"><span class="mark"></span>Brindle Cove Abodes</div>
<p class="abs foot-text">Nemo enim ipsam voluptatem quia voluptas sit aspernatur aut odit aut fugit, sed quia consequuntur magni dolores eos qui ra tione voluptatem sequi nesciunt. Neque porro quisquam est, qui dolorem ipsum quia dolor sit amet, consectetur, adipisci velit, sed quia non numquam eius modi tempora incidunt ut labore et dolore magnam aliquam quaerat voluptatem.</p>
<div class="abs links" style="left:711px;top:4418px">
  <h5>QUICK LINKS</h5>
  <ul><li>HOME</li><li>ABOUT</li><li>SERVICES</li><li>GALLERY</li><li>TESTIMONIALS</li><li>AWARDS</li><li>CONTACT US</li></ul>
</div>
<div class="abs links" style="left:936px;top:4418px">
  <h5>TOP LINKS</h5>
  <ul><li>NUMQUAM</li><li>EIUS MODI</li><li>TEMPORA</li><li>INCIDUNT UT</li><li>LABORE</li><li>TEMPORA</li><li>INCIDUNT UT</li></ul>
</div>
<div class="abs" style="left:172px;top:4744px;width:855px;height:1px;background:#777"></div>
<div class="abs copy">Copyrights @ 2021 Brindle Cove Abodes. All Rights Reserved.</div>

</body>
</html>
```